VELDRA WEBSITE

need to create a new website for VELDRA ltd
the company deals with all aspects of safety products & safety wear
we need a simple website to show
ideas can be taken from following website whose products we shall distribute in kenya
www.kwt.co.uk
www.torvik.eu
www.brimontgearhouse.com
www.gardovasupply.co.za

we need following tabs
1) home - basic company information
2) products - broken down to following categories ie gloves, head protection, ear protection, mouth protection, foot protection
3) contacts

the company profile is a reputable company dealing with all aspects of safety, HSE (health and safety equipment), and PPE (personal protective equipment)

the website should have the torvik logo for which we are an authorized distributor.
the torvi industrial range writeup can be picked from their website

Dear Designers, i shall be able to choose a final design in 2 weeks, sorry i have not been able to finalise this due to a personal reason

Target Market(s)

the buyers are all types of industry who care for their employees safety

Industry/Entity Type

Industrial

Requirements
Must have
• clean look, fresh look, user freindly
Nice to have
• clear images, quick links etc

```html
<!DOCTYPE html>
<html lang="en">
<head>
<meta charset="utf-8">
<title>VELDRA — Safety Gear Specialists</title>
<link href="https://fonts.googleapis.com/css2?family=Lato:wght@400;700;900&family=Open+Sans:wght@400;800&display=swap" rel="stylesheet">
<style>
:root{
  --yellow:#ffc600;
  --dark:#2e2e2e;
  --darker:#262626;
  --ink:#333333;
  --text:#555555;
  --line:#e3e3e3;
  --footer-text:#a8a8a8;
  --cream:#fffbe8;
}
*{margin:0;padding:0;box-sizing:border-box}
html,body{width:1088px;height:1200px;overflow:hidden}
body{position:relative;background:#fff;font-family:'Lato',sans-serif;color:var(--ink)}
.abs{position:absolute}
.backdrop{left:0;top:0;width:1088px;height:910px;background:var(--dark)}
.search{left:905px;top:0;width:20px;height:20px;background:#d8d8d8}
.header{left:154px;top:22px;width:773px;height:76px;background:var(--yellow)}
.brand{left:44px;top:0;width:151px;height:76px;background:var(--cream);display:flex;align-items:center;justify-content:center;gap:8px;font-weight:900;font-size:23px;color:#14303f;letter-spacing:1px}
.brand i{width:14px;height:14px;background:#14303f;display:block}
.nav a{position:absolute;top:33px;font-weight:700;font-size:14px;color:#333;text-decoration:none}
.nav-active{width:62px;height:3px;background:#fff}
.panel{left:154px;top:111px;width:773px;height:799px;background:#fff}
.tag{left:198px;top:125px;width:151px;height:18px;background:#1d2a33;color:var(--yellow);font-family:'Open Sans',sans-serif;font-weight:800;font-size:6.5px;line-height:8px;padding:1px 6px;letter-spacing:.4px}
.tag::before{content:"";position:absolute;left:0;top:0;right:0;height:1px;background:var(--yellow)}
.headline{left:197px;top:195px;font-family:'Open Sans',sans-serif;font-weight:800;font-size:37px;line-height:37px;color:#2f2f2f}
.headline span{color:var(--yellow)}
.hero-photo{left:517px;top:131px;width:360px;height:262px;background:radial-gradient(ellipse at 50% 45%,#e8d96a 0%,#c9b65a 40%,#fff 72%)}
.dots{left:849px;top:122px;display:flex;gap:6px}
.dots i{width:8px;height:8px;border-radius:50%;background:var(--yellow);opacity:.6}
.dots i:first-child{opacity:1}
.hline{height:1px;background:var(--line)}
.strap{left:199px;top:426px;font-weight:700;font-size:15px;color:#333}
.products-tab{left:642px;top:394px;width:241px;height:77px;background:var(--yellow);font-weight:900;font-size:15px;color:#3a3a3a;display:flex;align-items:center;justify-content:center}
.intro{left:198px;top:497px;width:420px;font-size:10px;line-height:15.4px;letter-spacing:.85px;color:var(--text);text-align:justify}
.intro p{margin-bottom:15.5px}
.btn{display:inline-flex;align-items:center;justify-content:center;font-size:10px;height:18px;padding:0 8px;text-decoration:none}
.btn-dark{left:199px;top:662px;background:#3a3a3a;color:#fff}
.cat-list{left:671px;top:495px;list-style:none}
.cat-list li{height:33.5px;display:flex;align-items:flex-start;font-size:10.5px;letter-spacing:.8px;color:#333}
.cat-list li b{width:22px;height:22px;background:#333;color:#fff;font-weight:400;font-size:15px;display:flex;align-items:center;justify-content:center;margin-right:19px}
.cat-list li span{margin-top:5px}
.sellers{left:198px;top:714px;width:455px;height:75px;border:1px solid var(--line);border-bottom:none;font-weight:700;font-size:15px;padding:29px 0 0 10px}
.partner{left:654px;top:714px;width:229px;height:75px;border:1px solid var(--line);border-left:none;border-bottom:none;display:flex;flex-direction:column;align-items:center;justify-content:center;color:#8d8d8d}
.partner b{font-size:21px;font-weight:900;line-height:22px}
.partner small{font-size:7px;font-weight:700;letter-spacing:.2px}
.grid{left:198px;top:789px;width:685px;display:grid;grid-template-columns:repeat(6,1fr)}
.grid .cell{border-right:1px solid var(--line);border-bottom:1px solid var(--line)}
.grid .cell:first-child{border-left:1px solid var(--line)}
.grid h4{background:var(--yellow);font-size:9.5px;font-weight:400;color:#333;text-align:center;height:18px;line-height:18px;white-space:nowrap}
.grid .thumb{height:83px;display:flex;align-items:center;justify-content:center}
.grid .thumb div{width:46px;height:66px;border-radius:10px}
.footer{left:154px;top:910px;width:773px;height:244px;background:var(--darker)}
.f-head{top:948px;font-weight:700;font-size:15px;color:#9d9d9d}
.f-text{top:1001px;font-size:12px;line-height:14.5px;color:var(--footer-text)}
.f-line{height:1px;background:#3c3c3c}
.btn-yellow{top:1098px;background:var(--yellow);color:#333}
.social{top:1019px;width:31px;height:31px;border-radius:50%;background:#3e3e3e;display:flex;align-items:center;justify-content:center}
.f-brand{top:1092px;color:#666;text-align:center;font-weight:900;font-size:17px;line-height:17px}
.f-brand small{display:block;font-size:6px;font-weight:400;letter-spacing:1px}
.shadow{left:154px;top:1154px;width:773px;height:46px;background:linear-gradient(#d9d9d9,#fff)}
.copy{left:0;width:1088px;top:1172px;text-align:center;font-size:9px;color:#555}
</style>
</head>
<body>
<div class="abs backdrop"></div>
<div class="abs search">
  <svg width="20" height="20" viewBox="0 0 20 20"><circle cx="9" cy="9" r="4.5" fill="none" stroke="#333" stroke-width="2"/><line x1="12.2" y1="12.2" x2="16" y2="16" stroke="#333" stroke-width="2.4"/></svg>
</div>

<header class="abs header">
  <div class="abs brand"><i></i>VELDRA</div>
  <div class="abs nav-active" style="left:459px;top:-2px"></div>
  <nav class="nav">
    <a style="left:469px">HOME</a>
    <a style="left:552px">PRODUCTS</a>
    <a style="left:667px">CONTACT</a>
  </nav>
</header>

<main class="abs panel"></main>
<div class="abs tag">SPECIALIZED PROTECTIVE<br>&amp; INDUSTRIAL PRODUCTS</div>
<h1 class="abs headline">BETTER<br>PROTECTION<br><span>BETTER VALUE</span></h1>
<div class="abs hero-photo" role="img" aria-label="Worker in a yellow hard hat, safety goggles and hi-vis vest"></div>
<div class="abs dots"><i></i><i></i><i></i></div>

<div class="abs hline" style="left:154px;top:393px;width:773px"></div>
<h2 class="abs strap">KENYA’S SAFTEY GEAR SPECIALISTS</h2>
<div class="abs products-tab">OUR PRODUCTS</div>
<div class="abs hline" style="left:154px;top:471px;width:773px"></div>

<div class="abs intro">
  <p>Duis fringilla dapibus justo, ut congue ligula venenatis sed. In euismod risus eget mi vestibulum a interdum sem commodo. Ut fermentum felis et massa sot.</p>
  <p>Quisque ultricies leo id felis porttitor eu sagittis orci imperdiet. Nulla vitae odio quis massa condimentum venenatis. Ut fermentum felis et massa sodales sit amet auctor urna pulvinar. In faucibus neque egestas ipsum lacinia lacinia.</p>
  <p>Quisque ultricies leo id felis porttitor eu sagittis orci imperdiet. Nulla vitae odio quis massa condimentum venenatis. Ut fermentum felis et massa sodales.</p>
</div>
<a class="abs btn btn-dark">READ MORE</a>

<ul class="abs cat-list">
  <li><b>+</b><span>GLOVES</span></li>
  <li><b>+</b><span>HEAD PROTECTION</span></li>
  <li><b>+</b><span>EAR PROTECTION</span></li>
  <li><b>+</b><span>MOUTH PROTECTION</span></li>
  <li><b>+</b><span>FOOT PROTECTION</span></li>
  <li><b>+</b><span>EYE PROTECTION</span></li>
</ul>

<div class="abs hline" style="left:154px;top:714px;width:773px"></div>
<h3 class="abs sellers">TOP SELLERS</h3>
<div class="abs partner"><b>Torvik</b><small>AUTHORIZED DISTRIBUTOR</small></div>

<div class="abs grid">
  <div class="cell"><h4>GLOVES</h4><div class="thumb"><div role="img" aria-label="Work gloves" style="background:linear-gradient(#f2a91c,#2b2b2b)"></div></div></div>
  <div class="cell"><h4>HEAD PROTECTION</h4><div class="thumb"><div role="img" aria-label="Welding helmet" style="background:linear-gradient(#6a6a78,#1f1f26)"></div></div></div>
  <div class="cell"><h4>EAR PROTECTION</h4><div class="thumb"><div role="img" aria-label="Ear defenders" style="background:linear-gradient(#333,#f3c21a)"></div></div></div>
  <div class="cell"><h4>MOUTH PROTECTION</h4><div class="thumb"><div role="img" aria-label="Respirator mask" style="background:linear-gradient(#9a9a9a,#e3d64a)"></div></div></div>
  <div class="cell"><h4>FOOT PROTECTION</h4><div class="thumb"><div role="img" aria-label="Safety boot" style="background:linear-gradient(#3a3a3a,#111)"></div></div></div>
  <div class="cell"><h4>EYE PROTECTION</h4><div class="thumb"><div role="img" aria-label="Face shield" style="background:linear-gradient(#f5cf23,#e9eef2)"></div></div></div>
</div>

<footer class="abs footer"></footer>
<h3 class="abs f-head" style="left:197px">CUSTOMER SERVICES</h3>
<h3 class="abs f-head" style="left:441px">CONTACT</h3>
<h3 class="abs f-head" style="left:686px">SHARE</h3>
<div class="abs f-line" style="left:197px;top:987px;width:690px"></div>
<div class="abs f-text" style="left:197px">Our Distribution<br>Useful Links<br>Advanced Search<br>Knowledge Base</div>
<div class="abs f-text" style="left:441px">48 Kiriba Road<br>Nairobi, KB 40318<br>E -mail: info@veldra.com<br>Telephone: +1 800 555 0142</div>
<div class="abs social" style="left:697px"></div>
<div class="abs social" style="left:765px"></div>
<div class="abs social" style="left:833px">
  <svg width="16" height="12" viewBox="0 0 16 12"><rect x="0.5" y="0.5" width="15" height="11" fill="#9a9a9a"/><polyline points="0.5,0.5 8,6.5 15.5,0.5" fill="none" stroke="#3e3e3e" stroke-width="1.5"/></svg>
</div>
<div class="abs f-line" style="left:197px;top:1076px;width:690px"></div>
<a class="abs btn btn-yellow" style="left:197px">READ MORE</a>
<a class="abs btn btn-yellow" style="left:441px">CONTACT US</a>
<div class="abs f-brand" style="left:684px;width:110px">Torvik<small>AUTHORIZED DISTRIBUTOR</small></div>
<div class="abs f-brand" style="left:812px;width:74px;top:1100px;font-size:13px">VELDRA</div>

<div class="abs shadow"></div>
<p class="abs copy">© &nbsp;2013 - Veldra</p>
</body>
</html>
```